Clean professional design needed for landscape property business

We need a logo for a new lawncare, landscaping , property maintenance business called Meadow Trim.
Our services include lawn mowing, garden maintenance, clean ups and some property maintenance.
We want a double sided business card that is clean and very professional using the colour scheme from our logo which is provided.
the business card should have impact as we will use these to drop into people's letterboxes as a marketing drop.
Initially we want to see what you come up with so there is a very wide scope here to work with.
Updates

Project Deadline Extended
Reason: we feel our original deadline was too short. we have extended to give more time for quality submissions.

Target Market(s)

High end property owners who don't wish to do there own gardneing or property maintenance

Industry/Entity Type

Business

Contact Information for Business Card

Name
Postion/ Title
Phone number
mobile
web address
physical address

services offered

Font styles to use
Sans Serif

Requirements
Must have
• curved edges preferrred
Nice to have
• We like the idea of the logo being embossed or etched into the card so it looks like it is below the surface of the card
Should not have
• No stock images or characters.

```html
<!DOCTYPE html>
<html lang="en">
<head>
<meta charset="utf-8">
<title>Meadow Trim – Business Card Die-Cut Layout</title>
<link rel="stylesheet" href="https://fonts.googleapis.com/css2?family=Didact+Gothic&family=Open+Sans:wght@400;700&display=swap">
<style>
  :root {
    --grass: #8cb034;
    --paper: #ffffff;
    --ink: #222222;
    --contact-ink: #555555;
    --rule: #6b6b6b;
    --frame: #a8a8a8;
    --ghost: #ececee;
  }
  * { margin: 0; padding: 0; box-sizing: border-box; }
  html, body { width: 1200px; height: 1200px; overflow: hidden; background: var(--paper); }
  .sheet {
    position: relative;
    width: 1200px; height: 1200px;
    border: 1px solid var(--frame);
    font-family: "Open Sans", sans-serif;
  }
  .card {
    position: absolute;
    border: 1px solid var(--rule);
    display: flex;
  }
  .panel { position: relative; height: 100%; }
  .panel--green { background: var(--grass); }
  .panel--white { background: var(--paper); }
  .panel + .panel { border-left: 1px solid var(--rule); }

  .label {
    position: absolute;
    font-family: "Didact Gothic", sans-serif;
    color: var(--ink);
    line-height: 1;
    white-space: nowrap;
  }
  .label--view { font-size: 42px; }
  .label--cut { font-size: 40px; }

  .die-cut {
    position: absolute;
    border-radius: 50%;
  }
  .die-cut--white { background: var(--paper); }
  .die-cut--ghost { background: var(--ghost); }

  .brand {
    position: absolute;
    display: flex;
    align-items: center;
    color: var(--paper);
    font-family: "Open Sans", sans-serif;
    font-weight: 700;
    white-space: nowrap;
    letter-spacing: -0.02em;
  }
  .brand__mark { background: var(--paper); margin-left: 0.35em; }
  .brand--small { font-size: 24px; }
  .brand--small .brand__mark { width: 9px; height: 9px; }
  .brand--large { font-size: 62px; }
  .brand--large .brand__mark { width: 20px; height: 20px; }

  .contact {
    position: absolute;
    right: 50px; top: 36px;
    text-align: right;
    color: var(--contact-ink);
    font-size: 19px;
    line-height: 34.5px;
  }
  .contact__name { font-weight: 700; }

  .arrows { position: absolute; inset: 0; pointer-events: none; }
</style>
</head>
<body>
<main class="sheet">

  <!-- Side A, folded closed -->
  <section class="card card--closed" style="left:375px; top:40px; width:486px; height:270px;">
    <div class="panel panel--green" style="width:242px;">
      <div class="die-cut die-cut--white" style="left:66px; top:60px; width:110px; height:110px;" role="img" aria-label="Die-cut window"></div>
      <div class="brand brand--small" style="left:24px; top:214px;">Meadow Trim<span class="brand__mark"></span></div>
    </div>
    <div class="panel panel--white" style="flex:1;"></div>
  </section>
  <p class="label label--cut" style="left:238px; top:58px;">CUT</p>
  <p class="label label--view" style="left:378px; top:314px;">A side close</p>

  <!-- Side A, opened -->
  <section class="card card--open-a" style="left:242px; top:426px; width:729px; height:270px;">
    <div class="panel panel--white" style="width:243px;">
      <div class="die-cut die-cut--ghost" style="left:70px; top:66px; width:106px; height:106px;" role="img" aria-label="Die-cut window seen from inside"></div>
    </div>
    <div class="panel panel--white" style="flex:1;">
      <div class="contact">
        <p class="contact__name">Name</p>
        <p>Postion/ Title</p>
        <p>Phone number</p>
        <p>mobile</p>
        <p>web address</p>
        <p>physical address</p>
      </div>
    </div>
  </section>
  <p class="label label--cut" style="left:104px; top:472px;">CUT</p>
  <p class="label label--view" style="left:256px; top:720px;">A side open</p>

  <!-- Side B, opened -->
  <section class="card card--open-b" style="left:246px; top:828px; width:728px; height:270px;">
    <div class="panel panel--green" style="width:486px;">
      <div class="brand brand--large" style="left:46px; top:104px;">Meadow Trim<span class="brand__mark"></span></div>
    </div>
    <div class="panel panel--green" style="flex:1;">
      <div class="die-cut die-cut--white" style="left:62px; top:66px; width:110px; height:110px;" role="img" aria-label="Die-cut window"></div>
    </div>
  </section>
  <p class="label label--cut" style="left:1018px; top:832px;">CUT</p>
  <p class="label label--view" style="left:266px; top:1106px;">b side open</p>

  <svg class="arrows" width="1200" height="1200" viewBox="0 0 1200 1200" aria-hidden="true">
    <defs>
      <marker id="arrowhead" viewBox="0 0 10 10" refX="8" refY="5" markerWidth="4.5" markerHeight="4.5" orient="auto">
        <path d="M0 0 L10 5 L0 10 Z" fill="#222"/>
      </marker>
    </defs>
    <g stroke="#222" stroke-width="4" fill="none" marker-end="url(#arrowhead)">
      <line x1="294" y1="112" x2="440" y2="146"/>
      <line x1="160" y1="526" x2="308" y2="558"/>
      <line x1="1076" y1="882" x2="932" y2="918"/>
    </g>
  </svg>
</main>
</body>
</html>
```